Cool modern, tech Business card design

Looking for a new business card design for our Managed IT Services company. We would like 2 sides, with the logo one one side horizontally and then the information on the back in either vertical or horizontal. We want our colors from the logo incorporated but also would like to see the color gray in there as well.

Target Market(s)

IT, Information Technology, Tech, Service

Industry/Entity Type

It Service

Contact Information for Business Card

Carl Penner
Managing Partner
(P)555-271-4830 ext xxx
(F)555-271-4831
www.brixtelcore.com

Font styles to use
Sans Serif

Colors
959595
000000
ec1f27

Requirements
Must have
• Logo on one side with some nice design or pattern
• Information on back in either vertical or horizontal format
Nice to have
• For it to look cool, tech, modern, stand out.

```html
<!DOCTYPE html>
<html lang="en">
<head>
<meta charset="utf-8">
<title>Brixtelcore Business Card</title>
<link href="https://fonts.googleapis.com/css2?family=Roboto:wght@400;500;700&display=swap" rel="stylesheet">
<style>
  :root {
    --brand-red: #ec1f27;
    --deep-red: #a8141c;
    --ink: #1a1a1a;
    --gray: #959595;
    --card: #f4f4f4;
    --backdrop: #2b2b2b;
  }
  * { box-sizing: border-box; margin: 0; padding: 0; }
  html, body { width: 1200px; height: 997px; overflow: hidden; }
  body {
    background: var(--backdrop);
    font-family: "Roboto", Arial, sans-serif;
    position: relative;
  }
  .card {
    position: absolute;
    top: 344px;
    width: 540px;
    height: 309px;
    background: linear-gradient(180deg, #ffffff 0%, var(--card) 100%);
    border-radius: 4px;
    box-shadow: 0 10px 30px rgba(0,0,0,0.5);
    overflow: hidden;
  }
  .card--front { left: 40px; }
  .card--back { left: 620px; }

  /* Front */
  .front-brand {
    position: absolute;
    left: 0; right: 0; top: 110px;
    text-align: center;
  }
  .wordmark {
    display: inline-block;
    font-weight: 700;
    font-size: 44px;
    letter-spacing: -1px;
    color: var(--ink);
  }
  .tagline {
    margin-top: 8px;
    font-size: 15px;
    letter-spacing: 2px;
    color: #555;
  }
  .tagline .accent { color: var(--brand-red); }

  /* Back */
  .back-brand {
    position: absolute;
    top: 58px; left: 0; right: 0;
    text-align: center;
  }
  .back-brand .wordmark { font-size: 38px; }
  .rule {
    position: absolute;
    left: 146px; right: 30px; top: 128px;
    height: 1px;
    background: var(--ink);
  }
  .person {
    position: absolute;
    left: 28px; top: 119px;
  }
  .person__name {
    font-weight: 700;
    font-size: 15px;
    color: var(--deep-red);
    text-transform: uppercase;
  }
  .person__role { font-size: 12px; color: var(--ink); margin-top: 2px; }
  .contacts {
    position: absolute;
    left: 28px; top: 172px;
    list-style: none;
  }
  .contacts li {
    display: flex; align-items: center; gap: 12px;
    font-size: 13px; color: var(--ink);
    height: 23px;
  }
  .contacts svg { width: 14px; height: 14px; }
  .address {
    position: absolute;
    right: 24px; top: 158px;
    text-align: right;
    font-size: 12px;
    line-height: 15px;
    color: var(--deep-red);
  }
  .card-base { position: absolute; left: 0; top: 0; width: 540px; height: 309px; }
  .website {
    position: absolute;
    right: 24px; top: 232px;
    font-size: 13px; font-weight: 700;
    letter-spacing: 1.5px;
    color: #fff;
  }
</style>
</head>
<body>

  <section class="card card--front" aria-label="Card front">
    <div class="front-brand">
      <div class="wordmark">brixtelcore</div>
      <p class="tagline">Innovative Managed <span class="accent">IT</span> Services</p>
    </div>
  </section>

  <section class="card card--back" aria-label="Card back">
    <svg class="card-base" viewBox="0 0 540 309" aria-hidden="true">
      <path d="M0 268 L232 268 Q244 268 250 258 L254 252 L262 252 L256 264 Q248 278 232 278 L0 278 Z" fill="#1a1a1a"/>
      <path d="M0 286 L0 309 L540 309 L540 220 L300 220 Q284 220 276 234 L266 254 Q258 286 236 286 Z" fill="var(--deep-red)"/>
    </svg>

    <div class="back-brand">
      <div class="wordmark">brixtelcore</div>
    </div>
    <div class="rule"></div>

    <div class="person">
      <p class="person__name">Carl Penner</p>
      <p class="person__role">Managing Partner</p>
    </div>

    <ul class="contacts">
      <li>
        <svg viewBox="0 0 14 14" aria-hidden="true"><circle cx="7" cy="7" r="7" fill="var(--deep-red)"/><path d="M4 5 Q7 3 10 5 L9 6.5 L8 6 L6 6 L5 6.5 Z M4.5 7 h5 v3 h-5 Z" fill="#fff"/></svg>
        555-271-4830
      </li>
      <li>
        <svg viewBox="0 0 14 14" aria-hidden="true"><circle cx="7" cy="7" r="7" fill="var(--deep-red)"/><rect x="3.5" y="4.5" width="7" height="5" fill="none" stroke="#fff" stroke-width="1"/><path d="M3.5 4.5 L7 7.5 L10.5 4.5" fill="none" stroke="#fff" stroke-width="1"/></svg>
        carl@brixtelcore.com
      </li>
      <li>
        <svg viewBox="0 0 14 14" aria-hidden="true"><circle cx="7" cy="7" r="7" fill="var(--deep-red)"/><circle cx="7" cy="7" r="3" fill="none" stroke="#fff" stroke-width="1.2"/></svg>
        carlpenner
      </li>
    </ul>

    <p class="address">14 Harlow Lane, Springfield<br>AB1 2CD, United Kingdom</p>
    <p class="website">www.brixtelcore.com</p>
  </section>

</body>
</html>
```